Video Learning Web Application Site Design

We are a new company that produce and distribute educational videos using a subscription model on our website. The videos are streamed on our website and users can tailor their own course packages by creating playlists. Each video-lesson are also split into several smaller segments, and it should be easy to find and play those segments.

Please note that both the screenshots and wireframes provided are only how it looks right now, if you as the designer have a better idea on how to present it then please share it.
Updates

Please view the screenshots as well, I believe I forgot to include two buttons on the wireframes that should be on the Our Courses page. Also, there is no need to make a carbon copy of the wireframes/screenshots, I'd like you designers to come up with a better way of displaying the information if possible. For inspiration you can look at sites like ClipNest (I like the simplicity of their design) and to some extent the Prism UI where they divide different areas of the page into clear "zones".

Thanks,

Reason: I have to extend the deadline because I've been really ill the last week. Will go through the current submissions now and provide feedback and looking forward to more submissions.

Target Market(s)

College and University students. Professionals wanting to expand their knowledge and people that want to learn new skills to get a promotion/new job.

Industry/Entity Type

Tailor

Requirements
Must have
• Must include the logo from the file "brightleaf-logo".
• Should include two pages, one of the video-player page and one of the course list.
• Try to incorporate the colors from the logo.
• Please note: If you look at the video-player.png file just below "Starte Tavla, bruke..." there are two rows, those are sub-parts of the lesson. Both these and the main lesson itself must have some easy way to Play and Add to Playlist.
Nice to have
• We prefer flat design, with simple and clean icons. Don't overdo the colors, stay within 3-4 colors with variations of them.
Should not have
• 3D-like elements, lot of shadows or hard to ready text.

```html
<!DOCTYPE html>
<html lang="en">
<head>
<meta charset="utf-8">
<title>brightleaf – Course Player</title>
<link href="https://fonts.googleapis.com/css2?family=Ubuntu:wght@400;500;700&display=swap" rel="stylesheet">
<style>
:root{
  --ink:#222;
  --navy:#0b4a63;
  --brand:#1a7ab5;
  --active:#0e89c5;
  --sky:#a6d6ec;
  --sky-cell:#7fc2e2;
  --sky-dark:#0d5f86;
  --green:#8dc63f;
  --green-cell:#a4d25a;
  --orange:#f7941d;
  --red:#f07070;
  --side:#0b0b0b;
  --side-line:#1e1e1e;
  --gray-bg:#f3f2f2;
  --muted:#8c8c8c;
  --link:#0b4a8a;
}
*{box-sizing:border-box;margin:0;padding:0}
html,body{width:1200px;height:778px;overflow:hidden}
body{font-family:"Ubuntu",sans-serif;color:var(--ink);background:#fff;position:relative;font-size:12px}
svg{display:block}
/* header */
.header{position:absolute;left:0;top:0;width:1200px;height:67px;border-bottom:4px solid var(--navy);background:#fff}
.brand{position:absolute;left:16px;top:14px;display:flex;align-items:center;gap:10px}
.brand-dot{width:34px;height:34px;border-radius:50%;background:var(--brand)}
.brand-name{font-size:34px;font-weight:500;color:var(--brand);letter-spacing:.5px;line-height:1}
.session{position:absolute;right:74px;top:17px;display:flex;align-items:center;gap:9px;font-size:11.5px}
.btn-logout{background:var(--green);color:#fff;width:94px;height:17px;line-height:17px;text-align:center;font-size:11px}
.nav{position:absolute;left:628px;top:43px;height:23px;width:498px;background:var(--navy);display:flex;align-items:center;color:#fff;font-size:11.5px}
.nav .burger{width:34px;height:100%;display:flex;align-items:center;justify-content:center;border-right:1px solid #2d6c86}
.nav .item{height:100%;display:flex;align-items:center;justify-content:center;border-right:1px solid #2d6c86}
.nav .search{margin-left:6px;width:153px;height:16px;background:#fff}
.nav .search-btn{width:24px;height:18px;margin-left:1px;background:var(--brand);display:flex;align-items:center;justify-content:center}
/* sidebar */
.sidebar{position:absolute;left:0;top:71px;width:255px;height:707px;background:var(--side);color:#fff}
.side-head{height:40px;display:flex;align-items:center;padding-left:10px;font-size:20px;font-weight:400;border-bottom:1px solid var(--side-line)}
.side-row{display:flex;align-items:center;height:34px;border-bottom:1px solid var(--side-line);font-size:12.5px;position:relative}
.side-row .ico{width:40px;height:100%;display:flex;align-items:center;justify-content:center;border-right:1px solid var(--side-line)}
.side-row .label{padding-left:10px;flex:1}
.side-row.active{background:var(--sky-dark)}
.badge{width:24px;height:19px;line-height:19px;text-align:center;font-size:11px;margin-right:11px;color:#fff}
.badge.orange{background:var(--orange)}
.badge.green{background:var(--green)}
.sub-list{margin-left:40px;border-left:1px solid var(--side-line)}
.sub-row{height:27.4px;display:flex;align-items:center;gap:7px;padding-left:3px;font-size:11.5px;border-bottom:1px solid var(--side-line);position:relative}
.sub-row .thumb{width:20px;height:20px}
.sub-row.current{background:var(--active)}
.sub-row.current::after{content:"";position:absolute;right:0;top:7px;border:7px solid transparent;border-right-color:#fff}
/* video */
.player{position:absolute;left:274px;top:90px;width:629px;height:361px}
.video-frame{width:100%;height:326px;background:linear-gradient(160deg,#e9e4de 0%,#c9a68a 35%,#7d8fa6 60%,#e2c3b2 85%,#f0ece8 100%)}
.controls{height:35px;background:#000;display:flex;align-items:center;padding:0 12px;gap:12px;color:#fff;font-size:10.5px}
.progress{flex:1;height:4px;background:#2a3a44;position:relative}
.progress span{position:absolute;left:0;top:0;height:100%;width:43%;background:var(--brand)}
/* course aside */
.course{position:absolute;left:925px;top:90px;width:210px}
.course-top{display:flex;gap:12px}
.course-thumb{width:51px;height:51px;background:linear-gradient(135deg,#c9d6de,#5f7f97)}
.course-title{font-weight:700;font-size:14px;margin-top:3px}
.course-sub{color:var(--muted);font-size:11.5px;line-height:13.5px;margin-top:2px}
.btn-remove{margin-top:15px;background:var(--red);color:#fff;width:100px;height:21px;line-height:21px;text-align:center;font-size:11px}
.aside-head{font-size:15.5px;margin:10px 0 3px 1px}
.link-list{width:198px;border-top:1px solid var(--sky)}
.link-row{display:flex;align-items:stretch;border-bottom:1px solid var(--sky);min-height:21px;font-size:11.5px;color:var(--link)}
.link-row .cell{width:20px;background:var(--sky-cell);display:flex;align-items:center;justify-content:center;border-right:1px solid #fff}
.link-row .txt{flex:1;padding:2px 0 2px 7px;display:flex;align-items:center;line-height:13px}
.link-row.on .cell{background:var(--sky-dark)}
.link-row.on .cell.play{background:var(--active)}
.link-row.on .txt{background:var(--sky)}
/* lower zone */
.lower{position:absolute;left:255px;top:470px;width:945px;height:308px;background:var(--gray-bg)}
.btn-cues{position:absolute;left:276px;top:484px;width:118px;height:22px;line-height:22px;text-align:center;background:var(--orange);color:#fff;font-size:11px}
.pager{position:absolute;left:801px;top:486px;width:101px;height:20px;background:#8a8a8a;color:#fff;font-size:10.5px;display:flex;align-items:center}
.pager .arr{width:20px;height:100%;display:flex;align-items:center;justify-content:center;background:#9d9d9d}
.pager .cnt{flex:1;text-align:center;border-left:1px solid #777;border-right:1px solid #777;line-height:20px}
.cue-list{position:absolute;left:276px;top:521px;width:609px}
.cue{display:flex;height:22.5px;border-bottom:1px solid var(--green);font-size:11.5px;align-items:stretch}
.cue .c{width:23px;display:flex;align-items:center;justify-content:center;background:var(--green-cell);border-right:1px solid #fff}
.cue .t{flex:1;display:flex;align-items:center;padding-left:8px}
.cue.open{background:var(--sky);border-bottom-color:var(--sky)}
.cue.open .c{background:var(--active)}
.cue.child{margin-left:23px;border-bottom-color:var(--sky);color:var(--link)}
.cue.child .c{background:var(--sky-cell)}
.cue.child.on .c{background:var(--sky-dark)}
.cue.child.on .c.play{background:var(--active)}
.cue.child.on .t{background:var(--sky)}
.scroll{position:absolute;left:896px;top:515px;width:5px;height:256px;background:#e1e1e1}
.scroll span{display:block;width:5px;height:135px;background:#a9a9a9}
.related{position:absolute;left:925px;top:485px;width:220px}
.related h2{font-size:19px;font-weight:400;margin-bottom:6px}
.rel-item{display:flex;gap:7px;height:35px}
.rel-thumb{width:27px;height:27px;background:linear-gradient(135deg,#c9d6de,#5f7f97)}
.rel-name{font-size:13px;color:#444;line-height:14px}
.rel-date{font-size:9px;color:var(--muted)}
</style>
</head>
<body>

<header class="header">
  <div class="brand"><div class="brand-dot"></div><span class="brand-name">brightleaf</span></div>
  <div class="session"><span>Logged in as Marlowe</span><span class="btn-logout">Log Out</span></div>
  <nav class="nav">
    <div class="burger"><svg width="14" height="11" viewBox="0 0 14 11" fill="#fff"><rect width="14" height="2"/><rect y="4.5" width="14" height="2"/><rect y="9" width="14" height="2"/></svg></div>
    <div class="item" style="width:69px">About</div>
    <div class="item" style="width:73px">Videos</div>
    <div class="item" style="width:62px">Help</div>
    <div class="item" style="width:75px">Options</div>
    <div class="search"></div>
    <div class="search-btn"><svg width="13" height="13" viewBox="0 0 13 13" fill="none" stroke="#fff" stroke-width="1.8"><circle cx="5.5" cy="5.5" r="4"/><path d="M8.5 8.5l3.5 3.5"/></svg></div>
  </nav>
</header>

<aside class="sidebar">
  <div class="side-head">Introduction</div>
  <div class="side-row"><div class="ico"><svg width="20" height="20" viewBox="0 0 20 20" fill="none" stroke="#fff" stroke-width="1.8"><circle cx="10" cy="10" r="8"/><path d="M7 13l2-5 4-1-2 5z" fill="#fff"/></svg></div><span class="label">Introduction</span><span class="badge orange">12</span></div>
  <div class="side-head" style="height:42px">Modules</div>
  <div class="side-row" style="height:36px"><div class="ico"><svg width="18" height="18" viewBox="0 0 18 18" fill="none" stroke="#fff" stroke-width="1.8"><rect x="7" y="2" width="9" height="9"/><path d="M5 6H2v10h10v-3"/></svg></div><span class="label">Our Courses</span></div>
  <div class="side-row active"><div class="ico"><svg width="18" height="18" viewBox="0 0 18 18" fill="none" stroke="#fff" stroke-width="1.8"><circle cx="9" cy="6" r="3.5"/><path d="M2.5 16.5c0-4 3-6 6.5-6s6.5 2 6.5 6z"/></svg></div><span class="label">Your Courses</span></div>
  <div class="sub-list">
    <div class="sub-row"><div class="thumb" style="background:#e07a1f"></div>DeskSuite 2013 - Beginner</div>
    <div class="sub-row current"><div class="thumb" style="background:#9fb6c6"></div>Tavla 2013 - Beginner</div>
    <div class="sub-row"><div class="thumb" style="background:#1b6fc9"></div>PixelForge 2013 - Beginner</div>
    <div class="sub-row"><div class="thumb" style="background:#3f9b3a"></div>Tavla 2013 - Advance</div>
    <div class="sub-row"><div class="thumb" style="background:#7a3fb0"></div>Tavla 2013 - Beginner</div>
  </div>
  <div class="side-row"><div class="ico"><svg width="18" height="18" viewBox="0 0 18 18" fill="none" stroke="#fff" stroke-width="1.8"><rect x="7" y="2" width="9" height="9"/><path d="M5 6H2v10h10v-3"/></svg></div><span class="label">Lorem Courses</span></div>
  <div class="side-head">Playlists</div>
  <div class="side-row"><div class="ico"><svg width="20" height="20" viewBox="0 0 20 20"><circle cx="10" cy="10" r="8" fill="none" stroke="#fff" stroke-width="1.8"/><path d="M8 6.5l5 3.5-5 3.5z" fill="#fff"/></svg></div><span class="label">My Playlist 01</span><span class="badge orange">12</span></div>
  <div class="side-row"><div class="ico"><svg width="20" height="20" viewBox="0 0 20 20"><circle cx="10" cy="10" r="8" fill="none" stroke="#fff" stroke-width="1.8"/><path d="M8 6.5l5 3.5-5 3.5z" fill="#fff"/></svg></div><span class="label">Lorem Playlist</span><span class="badge green">4</span></div>
  <div class="side-row"><div class="ico"><svg width="20" height="20" viewBox="0 0 20 20"><circle cx="10" cy="10" r="8" fill="none" stroke="#fff" stroke-width="1.8"/><path d="M8 6.5l5 3.5-5 3.5z" fill="#fff"/></svg></div><span class="label">Impsum Plays</span></div>
  <div class="side-row"><div class="ico"><svg width="20" height="20" viewBox="0 0 20 20"><circle cx="10" cy="10" r="8" fill="none" stroke="#fff" stroke-width="1.8"/><path d="M8 6.5l5 3.5-5 3.5z" fill="#fff"/></svg></div><span class="label">PlayList Doner 02</span><span class="badge orange">3</span></div>
</aside>

<section class="player">
  <div class="video-frame" role="img" aria-label="Video still: a group of smiling students holding notebooks"></div>
  <div class="controls">
    <svg width="12" height="14" viewBox="0 0 12 14" fill="#fff"><path d="M1 0l11 7-11 7z"/></svg>
    <div class="progress"><span></span></div>
    <span>1:04/4:30</span>
    <svg width="16" height="14" viewBox="0 0 16 14" fill="#fff"><path d="M0 4h4l5-4v14l-5-4H0z"/><path d="M11 3.5a5 5 0 010 7M13 1.5a8 8 0 010 11" stroke="#fff" stroke-width="1.4" fill="none"/></svg>
    <svg width="15" height="15" viewBox="0 0 15 15" fill="none" stroke="#fff" stroke-width="2"><path d="M1 5V1h4M10 1h4v4M14 10v4h-4M5 14H1v-4"/></svg>
  </div>
</section>

<aside class="course">
  <div class="course-top">
    <div class="course-thumb" role="img" aria-label="Course cover artwork"></div>
    <div><div class="course-title">Tavla 2013 - Beginner</div><div class="course-sub">Lorem Impsum proin<br>Impsum Text</div></div>
  </div>
  <div class="btn-remove">Remove Course</div>
  <div class="aside-head">Downloads</div>
  <div class="link-list">
    <div class="link-row"><div class="cell"><svg width="11" height="11" viewBox="0 0 12 12" fill="#fff"><path d="M6 0l1.8 4H12L8.6 6.6 10 11 6 8.3 2 11l1.4-4.4L0 4h4.2z"/></svg></div><div class="cell"><svg width="12" height="12" viewBox="0 0 12 12" fill="#fff"><path d="M5 0h2v5h2L6 8 3 5h2z"/><path d="M0 7h2v3h8V7h2v5H0z"/></svg></div><div class="txt">Download Lessons file (xls)</div></div>
    <div class="link-row"><div class="cell"><svg width="11" height="11" viewBox="0 0 12 12" fill="#fff"><path d="M6 0l1.8 4H12L8.6 6.6 10 11 6 8.3 2 11l1.4-4.4L0 4h4.2z"/></svg></div><div class="cell"><svg width="12" height="12" viewBox="0 0 12 12" fill="#fff"><path d="M5 0h2v5h2L6 8 3 5h2z"/><path d="M0 7h2v3h8V7h2v5H0z"/></svg></div><div class="txt">Download Study material sample (doc)</div></div>
  </div>
  <div class="aside-head" style="margin-top:4px">Cues</div>
  <div class="link-list">
    <div class="link-row"><div class="cell"><svg width="11" height="11" viewBox="0 0 12 12" fill="#fff"><path d="M6 0l1.8 4H12L8.6 6.6 10 11 6 8.3 2 11l1.4-4.4L0 4h4.2z"/></svg></div><div class="cell play"><svg width="8" height="9" viewBox="0 0 8 9" fill="#fff"><path d="M0 0l8 4.5L0 9z"/></svg></div><div class="txt">Ipsum dolor sit amet</div></div>
    <div class="link-row on"><div class="cell"><svg width="11" height="11" viewBox="0 0 12 12" fill="#fff"><path d="M6 0l1.8 4H12L8.6 6.6 10 11 6 8.3 2 11l1.4-4.4L0 4h4.2z"/></svg></div><div class="cell play"><svg width="8" height="9" viewBox="0 0 8 9" fill="#fff"><path d="M0 0l8 4.5L0 9z"/></svg></div><div class="txt">Lorem ipsum dolor sit amet consectetur adipiscing</div></div>
    <div class="link-row"><div class="cell"><svg width="11" height="11" viewBox="0 0 12 12" fill="#fff"><path d="M6 0l1.8 4H12L8.6 6.6 10 11 6 8.3 2 11l1.4-4.4L0 4h4.2z"/></svg></div><div class="cell play"><svg width="8" height="9" viewBox="0 0 8 9" fill="#fff"><path d="M0 0l8 4.5L0 9z"/></svg></div><div class="txt">Ipsum dolor sit amet</div></div>
    <div class="link-row"><div class="cell"><svg width="11" height="11" viewBox="0 0 12 12" fill="#fff"><path d="M6 0l1.8 4H12L8.6 6.6 10 11 6 8.3 2 11l1.4-4.4L0 4h4.2z"/></svg></div><div class="cell play"><svg width="8" height="9" viewBox="0 0 8 9" fill="#fff"><path d="M0 0l8 4.5L0 9z"/></svg></div><div class="txt">Consectetur adipiscing 4</div></div>
    <div class="link-row"><div class="cell"><svg width="11" height="11" viewBox="0 0 12 12" fill="#fff"><path d="M6 0l1.8 4H12L8.6 6.6 10 11 6 8.3 2 11l1.4-4.4L0 4h4.2z"/></svg></div><div class="cell play"><svg width="8" height="9" viewBox="0 0 8 9" fill="#fff"><path d="M0 0l8 4.5L0 9z"/></svg></div><div class="txt">Consectetur adipiscing Co-nsectetur adipiscing 4</div></div>
    <div class="link-row"><div class="cell"><svg width="11" height="11" viewBox="0 0 12 12" fill="#fff"><path d="M6 0l1.8 4H12L8.6 6.6 10 11 6 8.3 2 11l1.4-4.4L0 4h4.2z"/></svg></div><div class="cell play"><svg width="8" height="9" viewBox="0 0 8 9" fill="#fff"><path d="M0 0l8 4.5L0 9z"/></svg></div><div class="txt">Consectetur adipiscing 4</div></div>
  </div>
</aside>

<div class="lower"></div>
<div class="btn-cues">Show All Cues</div>
<div class="pager"><div class="arr"><svg width="6" height="8" viewBox="0 0 6 8" fill="#fff"><path d="M6 0v8L0 4z"/></svg></div><div class="cnt">1-10 of 50</div><div class="arr"><svg width="6" height="8" viewBox="0 0 6 8" fill="#fff"><path d="M0 0v8l6-4z"/></svg></div></div>

<div class="cue-list">
  <div class="cue"><div class="c"><svg width="11" height="11" viewBox="0 0 11 11" fill="#fff"><rect x="4.5" width="2" height="11"/><rect y="4.5" width="11" height="2"/></svg></div><div class="c"><svg width="11" height="11" viewBox="0 0 12 12" fill="#fff"><path d="M6 0l1.8 4H12L8.6 6.6 10 11 6 8.3 2 11l1.4-4.4L0 4h4.2z"/></svg></div><div class="c"><svg width="8" height="9" viewBox="0 0 8 9" fill="#fff"><path d="M0 0l8 4.5L0 9z"/></svg></div><div class="t">Item 0 Lorem Impsum</div></div>
  <div class="cue open"><div class="c"><svg width="11" height="11" viewBox="0 0 11 11" fill="#fff"><rect y="4.5" width="11" height="2"/></svg></div><div class="t">Item 1</div></div>
  <div class="cue child"><div class="c"><svg width="11" height="11" viewBox="0 0 12 12" fill="#fff"><path d="M6 0l1.8 4H12L8.6 6.6 10 11 6 8.3 2 11l1.4-4.4L0 4h4.2z"/></svg></div><div class="c play"><svg width="8" height="9" viewBox="0 0 8 9" fill="#fff"><path d="M0 0l8 4.5L0 9z"/></svg></div><div class="t">Ipsum dolor sit amet, consectet 0</div></div>
  <div class="cue child on"><div class="c"><svg width="11" height="11" viewBox="0 0 12 12" fill="#fff"><path d="M6 0l1.8 4H12L8.6 6.6 10 11 6 8.3 2 11l1.4-4.4L0 4h4.2z"/></svg></div><div class="c play"><svg width="8" height="9" viewBox="0 0 8 9" fill="#fff"><path d="M0 0l8 4.5L0 9z"/></svg></div><div class="t">Lorem ipsum dolor sit amet, consectetur adipiscing Child 2</div></div>
  <div class="cue child"><div class="c"><svg width="11" height="11" viewBox="0 0 12 12" fill="#fff"><path d="M6 0l1.8 4H12L8.6 6.6 10 11 6 8.3 2 11l1.4-4.4L0 4h4.2z"/></svg></div><div class="c play"><svg width="8" height="9" viewBox="0 0 8 9" fill="#fff"><path d="M0 0l8 4.5L0 9z"/></svg></div><div class="t">Por sit amet, consectetur adipiscing Childas</div></div>
  <div class="cue child"><div class="c"><svg width="11" height="11" viewBox="0 0 12 12" fill="#fff"><path d="M6 0l1.8 4H12L8.6 6.6 10 11 6 8.3 2 11l1.4-4.4L0 4h4.2z"/></svg></div><div class="c play"><svg width="8" height="9" viewBox="0 0 8 9" fill="#fff"><path d="M0 0l8 4.5L0 9z"/></svg></div><div class="t">Dolor sit amet, consectetur adipiscing Child 43</div></div>
  <div class="cue child"><div class="c"><svg width="11" height="11" viewBox="0 0 12 12" fill="#fff"><path d="M6 0l1.8 4H12L8.6 6.6 10 11 6 8.3 2 11l1.4-4.4L0 4h4.2z"/></svg></div><div class="c play"><svg width="8" height="9" viewBox="0 0 8 9" fill="#fff"><path d="M0 0l8 4.5L0 9z"/></svg></div><div class="t">Amet, consectetur adipiscing Child 4</div></div>
  <div class="cue"><div class="c"><svg width="11" height="11" viewBox="0 0 11 11" fill="#fff"><rect x="4.5" width="2" height="11"/><rect y="4.5" width="11" height="2"/></svg></div><div class="c"><svg width="11" height="11" viewBox="0 0 12 12" fill="#fff"><path d="M6 0l1.8 4H12L8.6 6.6 10 11 6 8.3 2 11l1.4-4.4L0 4h4.2z"/></svg></div><div class="c"><svg width="8" height="9" viewBox="0 0 8 9" fill="#fff"><path d="M0 0l8 4.5L0 9z"/></svg></div><div class="t">Item 0 Lorem Impsum</div></div>
  <div class="cue"><div class="c"><svg width="11" height="11" viewBox="0 0 11 11" fill="#fff"><rect x="4.5" width="2" height="11"/><rect y="4.5" width="11" height="2"/></svg></div><div class="c"><svg width="11" height="11" viewBox="0 0 12 12" fill="#fff"><path d="M6 0l1.8 4H12L8.6 6.6 10 11 6 8.3 2 11l1.4-4.4L0 4h4.2z"/></svg></div><div class="c"><svg width="8" height="9" viewBox="0 0 8 9" fill="#fff"><path d="M0 0l8 4.5L0 9z"/></svg></div><div class="t">Item 0 Lorem Impsum</div></div>
  <div class="cue"><div class="c"><svg width="11" height="11" viewBox="0 0 11 11" fill="#fff"><rect x="4.5" width="2" height="11"/><rect y="4.5" width="11" height="2"/></svg></div><div class="c"><svg width="11" height="11" viewBox="0 0 12 12" fill="#fff"><path d="M6 0l1.8 4H12L8.6 6.6 10 11 6 8.3 2 11l1.4-4.4L0 4h4.2z"/></svg></div><div class="c"><svg width="8" height="9" viewBox="0 0 8 9" fill="#fff"><path d="M0 0l8 4.5L0 9z"/></svg></div><div class="t">Item 0 Lorem Impsum</div></div>
  <div class="cue"><div class="c"><svg width="11" height="11" viewBox="0 0 11 11" fill="#fff"><rect x="4.5" width="2" height="11"/><rect y="4.5" width="11" height="2"/></svg></div><div class="c"><svg width="11" height="11" viewBox="0 0 12 12" fill="#fff"><path d="M6 0l1.8 4H12L8.6 6.6 10 11 6 8.3 2 11l1.4-4.4L0 4h4.2z"/></svg></div><div class="c"><svg width="8" height="9" viewBox="0 0 8 9" fill="#fff"><path d="M0 0l8 4.5L0 9z"/></svg></div><div class="t">Item 0 Lorem Impsum</div></div>
</div>
<div class="scroll"><span></span></div>

<aside class="related">
  <h2>Related Courses</h2>
  <div class="rel-item"><div class="rel-thumb"></div><div><div class="rel-name">DeskSuite Expert</div><div class="rel-date">June 2013</div></div></div>
  <div class="rel-item"><div class="rel-thumb"></div><div><div class="rel-name">PixelForge CS3 Pro</div><div class="rel-date">August 2012</div></div></div>
  <div class="rel-item"><div class="rel-thumb"></div><div><div class="rel-name">Tavla Advance 2013</div><div class="rel-date">May 2013</div></div></div>
  <h2 style="margin-top:2px">Recently Viewed</h2>
  <div class="rel-item"><div class="rel-thumb"></div><div><div class="rel-name">Playlist Editor 2014</div><div class="rel-date">June 2013</div></div></div>
  <div class="rel-item"><div class="rel-thumb"></div><div><div class="rel-name">Script Coder Pro 12</div><div class="rel-date">September 1998</div></div></div>
  <div class="rel-item"><div class="rel-thumb"></div><div><div class="rel-name">MotionLab CS3</div><div class="rel-date">May 2013</div></div></div>
</aside>

</body>
</html>
```